Lanterns Harvest Night flyer design contest

Name of event: Lantern’s Harvest Night

Tagline: ‘While the Queen’s away the staff will play’

Description: ‘…while the Queen is out celebrating her birthday with high tea, the palace staff are throwing a party at 14th loftspace and drinking her booze!

Date: Sunday 10th June 2012

Time: 8pm-3am

Dress code: Smart/casual or join in the theme

TICKETS
-Purchased through our website or social page, at the venue or at the door

Pre-Purchase Tickets: $10

Entry on the night (subject to availability): $15

Tickets Include:

Priority entry
Finger food from 9-10pm
‘Kir Royal’ cocktail on arrival

DRINK SPECIALS

$10 Kir Royal’s all night long!
$20 Valdoro buckets from 9-11pm

DJ's

Playing from 9-3am

Line up includes:

Dusky Amber
Tilted
DJ Marvek

Ph: (03) 9514 2760
Web: www.14thloftspace.com.au
Address: 14 Marlowe Lane St Kilda

I have attached an image which shows the feel that I am going for (plz see att.)

Reason: I wanted a 3 day deadline but this option was not available on the booking screen

Hi there,

If anyone finds a stock image that is appropriate you can add the low res to the mock up and if your design wins i can purchase the image to replace it (up to $20).. hope this helps :) Lira

Target Market(s)

Target Market is 20-35 year olds

Industry/Entity Type

Apartment

Requirements
Must have
• Must have a graphical/picture element to it
Also must have our company logo
Must have all the information listed in the task description
Must be a fun and cool design

```html
<!DOCTYPE html>
<html lang="en">
<head>
<meta charset="utf-8">
<title>Lantern’s Harvest Night – 14th loftspace</title>
<link href="https://fonts.googleapis.com/css2?family=Bangers&family=Lobster&family=Lobster+Two:ital,wght@1,700&family=Oswald:wght@500;600;700&family=Ubuntu:ital,wght@0,500;0,700;1,500&display=swap" rel="stylesheet">
<style>
  :root {
    --magenta: #e020c8;
    --magenta-soft: rgba(226, 40, 206, 0.82);
    --ink: #111111;
    --white: #ffffff;
    --paper: #ffffff;
    --photo-dark: #3e4a4c;
    --photo-mid: #8fa3a3;
    --photo-light: #c9d2cf;
    --jacket: #8a2a2e;
    --sofa: #c65a78;
    --sofa-light: #d88aa0;
    --etching-light: #e4e4e2;
    --etching-mid: #b9b9b6;
  }
  * { margin: 0; padding: 0; box-sizing: border-box; }
  html, body { width: 933px; height: 1200px; overflow: hidden; background: var(--paper); }
  .canvas { position: relative; width: 933px; height: 1200px; }
  .flyer {
    position: absolute; left: 56px; top: 20px;
    width: 775px; height: 1098px;
    transform: scale(1.058); transform-origin: 0 0;
    overflow: hidden; background: var(--etching-light);
    font-family: "Oswald", sans-serif;
  }
  .hero-backdrop {
    position: absolute; left: 0; top: 0; width: 775px; height: 515px;
    background: radial-gradient(ellipse at 45% 40%, var(--photo-light) 0%, var(--photo-mid) 45%, var(--photo-dark) 100%);
  }
  .hero-figure {
    position: absolute; left: 55px; top: 95px; width: 720px; height: 420px;
    border-radius: 60px 0 0 0;
    background:
      radial-gradient(ellipse 34% 55% at 42% 40%, var(--jacket) 0%, var(--jacket) 55%, rgba(138,42,46,0) 100%),
      radial-gradient(ellipse 90% 70% at 60% 75%, var(--sofa-light) 0%, var(--sofa) 55%, rgba(198,90,120,0) 100%);
  }
  .party-etching {
    position: absolute; left: 0; top: 515px; width: 775px; height: 583px;
    background: linear-gradient(160deg, var(--etching-light) 0%, var(--etching-mid) 55%, var(--etching-light) 100%);
  }
  .event-date { position: absolute; left: 16px; top: 42px; color: var(--white); line-height: 1; }
  .event-date .day-number {
    font-weight: 700; font-size: 60px;
    display: inline-block; vertical-align: top;
    text-shadow: 2px 2px 0 var(--magenta);
  }
  .event-date .day-detail { display: inline-block; vertical-align: top; margin-top: 6px; }
  .event-date .weekday, .event-date .month {
    display: block; font-weight: 700; color: var(--magenta);
    -webkit-text-stroke: 1px var(--white);
  }
  .event-date .weekday { font-size: 28px; }
  .event-date .month { font-size: 20px; }
  .event-time {
    position: absolute; left: 18px; top: 108px;
    font-weight: 700; font-size: 38px; color: var(--white);
    text-shadow: 2px 2px 0 var(--magenta);
  }
  .dress-code {
    position: absolute; left: 18px; top: 158px; width: 230px;
    font-family: "Lobster Two", cursive; font-style: italic; font-weight: 700;
    font-size: 21px; line-height: 30px; color: var(--ink);
  }
  .event-title {
    position: absolute; right: 18px; top: 12px; text-align: center;
    font-family: "Lobster", cursive; font-weight: 400;
    font-size: 60px; line-height: 66px; color: var(--white);
    -webkit-text-stroke: 1.5px var(--magenta);
    text-shadow: 3px 3px 0 var(--magenta);
  }
  .dj-panel {
    position: absolute; left: 533px; top: 185px; width: 232px; height: 216px;
    background: var(--magenta-soft); border-radius: 14px;
    padding: 6px 12px 0 8px; text-align: right; color: var(--ink);
    font-family: "Ubuntu", sans-serif; font-weight: 500;
  }
  .dj-panel .panel-heading { font-weight: 700; font-size: 28px; color: var(--white); line-height: 32px; }
  .dj-panel .play-times { font-size: 19px; line-height: 28px; }
  .dj-panel .play-times strong { color: var(--white); font-weight: 700; font-size: 22px; }
  .dj-panel .lineup-label { font-size: 19px; line-height: 28px; }
  .dj-panel .lineup { list-style: none; font-family: "Bangers", cursive; font-size: 31px; line-height: 41px; color: var(--white); letter-spacing: 0.5px; }
  .tagline {
    position: absolute; left: 0; width: 775px; top: 440px; text-align: center;
    font-family: "Bangers", cursive; font-size: 80px; line-height: 70px;
    color: var(--magenta); -webkit-text-stroke: 2px var(--white); letter-spacing: 1px;
  }
  .story {
    position: absolute; right: 15px; top: 598px; text-align: right;
    font-weight: 600; font-size: 24px; line-height: 33px; color: var(--ink);
  }
  .story .venue-name { color: var(--magenta); font-size: 32px; font-weight: 500; }
  .story .booze { font-size: 31px; }
  .tickets { position: absolute; left: 14px; top: 660px; width: 440px; color: var(--ink); }
  .tickets .section-heading { font-family: "Bangers", cursive; font-size: 44px; line-height: 46px; margin-left: 12px; }
  .tickets .ticket-terms { list-style: none; font-weight: 500; font-size: 18px; line-height: 22px; }
  .tickets .ticket-terms li { padding-left: 12px; text-indent: -12px; }
  .tickets .ticket-terms li::before { content: "• "; }
  .tickets .price { font-weight: 700; font-size: 30px; }
  .ticket-extras {
    position: absolute; left: 25px; top: 838px;
    font-family: "Ubuntu", sans-serif; font-weight: 700; color: var(--magenta);
    font-size: 18px; line-height: 25px;
  }
  .ticket-extras .extras-heading { font-style: italic; font-weight: 500; margin-bottom: 4px; }
  .ticket-extras ul { list-style: none; }
  .drink-specials {
    position: absolute; left: 482px; top: 820px; width: 280px; height: 105px;
    background: var(--magenta); border-radius: 12px; text-align: center;
    color: var(--white); font-family: "Ubuntu", sans-serif; font-weight: 700;
  }
  .drink-specials .panel-heading { font-family: "Lobster", cursive; font-weight: 400; font-size: 39px; line-height: 52px; }
  .drink-specials p { font-size: 15.5px; line-height: 22px; }
  .venue-name-mark {
    position: absolute; left: 20px; top: 990px;
    font-family: "Ubuntu", sans-serif; font-weight: 700; font-size: 38px; line-height: 1;
    color: var(--ink); display: flex; align-items: center; gap: 10px;
  }
  .venue-name-mark .mark-dot { width: 18px; height: 18px; border-radius: 50%; background: var(--ink); }
  .contact {
    position: absolute; right: 15px; top: 966px; text-align: right; font-style: normal;
    font-family: "Ubuntu", sans-serif; font-weight: 700; font-size: 24px; line-height: 35px; color: var(--ink);
  }
  .contact .web-link { color: var(--magenta); }
</style>
</head>
<body>
<div class="canvas">
  <div class="flyer">
    <div class="hero-backdrop" role="img" aria-label="Teal damask wallpaper backdrop"></div>
    <div class="hero-figure" role="img" aria-label="Photo of a young man in a red velvet jacket and sunglasses sipping wine while lounging on a pink tufted sofa"></div>
    <div class="party-etching" role="img" aria-label="Faded engraving of an old palace ball with guests in period dress"></div>

    <div class="event-date">
      <span class="day-number">10th</span>
      <span class="day-detail"><span class="weekday">Sunday</span><span class="month">June 2012</span></span>
    </div>
    <div class="event-time">8pm-3am</div>
    <p class="dress-code">Dress code:<br>Smart/casual or join<br>in the theme</p>

    <h1 class="event-title">Lantern’s<br>Harvest Night</h1>

    <section class="dj-panel">
      <h2 class="panel-heading">DJ's</h2>
      <p class="play-times">Playing from <strong>9-3am</strong></p>
      <p class="lineup-label">Line up includes:</p>
      <ul class="lineup">
        <li>Dusky Amber</li>
        <li>Tilted</li>
        <li>DJ Marvek</li>
      </ul>
    </section>

    <h2 class="tagline">While the Queen’s away<br>the staff will play!</h2>

    <p class="story">...while the Queen is out celebrating<br>her birthday with high tea, the palace<br>staff are throwing a PARTY at<br><span class="venue-name">14th loftspace</span> and<br><span class="booze">drinking her booze!</span></p>

    <section class="tickets">
      <h2 class="section-heading">Tickets</h2>
      <ul class="ticket-terms">
        <li>Purchased through our website<br>or social page, at the venue or<br>at the door</li>
        <li>Pre-Purchase Tickets: <span class="price">$10</span></li>
        <li>Entry on the night (subject to availability): <span class="price">$15</span></li>
      </ul>
    </section>

    <section class="ticket-extras">
      <p class="extras-heading">Tickets Include:</p>
      <ul>
        <li>Priority entry</li>
        <li>Finger food from 9-10pm</li>
        <li>‘Kir Royal’ cocktail on arrival</li>
      </ul>
    </section>

    <section class="drink-specials">
      <h2 class="panel-heading">Drink Specials</h2>
      <p>$10 Kir Royal’s all night long!</p>
      <p>$20 Valdoro buckets from 9-11pm</p>
    </section>

    <div class="venue-name-mark"><span class="mark-dot"></span>14th loftspace</div>

    <address class="contact">
      <p>Ph: (03) 9514 2760</p>
      <p>Web: <span class="web-link">www.14thloftspace.com.au</span></p>
      <p>Address: 14 Marlowe Lane St Kilda</p>
    </address>
  </div>
</div>
</body>
</html>
```